Business Card - Rebranding for Consulting Firm

We are renaming and rebranding our consulting firm and need to raise the level of quality of our cards as part of that effort. We consult to leading high tech, life science and other innovation sector companies.

Need a two-sided business card design.

Side 1: (a) Company logo (b) tag line: Optimize Your Investment in Talent (c) Name (d) Title (e) Phone 1: Office (f) Phone 2: Mobile (g) email: person@HollowmereAdvisory.com

Side 2: Two lines of text: (a) Growth is Imperative. Change is Constant. Talent Executes Strategy. (b) We help you excel at all three.

Target Market(s)

Business and human resources executives and senior managers

Industry/Entity Type

Management Consulting

Contact Information for Business Card

Font styles to use
Sans Serif

Requirements
Must have
• clean, not too busy, but with a bit of creativity. Stick to the colors used in the attached logo
• appeal to high tech, life science companies
Nice to have
• prefer white background

```html
<!DOCTYPE html>
<html lang="en">
<head>
<meta charset="utf-8">
<title>Hollowmere Advisory – Business Card</title>
<link rel="stylesheet" href="https://fonts.googleapis.com/css2?family=Exo+2:wght@700&family=Roboto:wght@400&family=Roboto+Condensed:wght@400&display=swap">
<style>
  :root {
    --stage: #e6e6e6;
    --brand-blue: #0b6099;
    --brand-blue-dark: #0a5a91;
    --brand-blue-text: #1d6aa3;
    --slate: #69737d;
    --card-white: #f7f7f7;
    --text-grey: #606a74;
    --divider: #d8d8d8;
    --on-blue: #ffffff;
  }
  * { margin: 0; padding: 0; box-sizing: border-box; }
  html, body { width: 1200px; height: 576px; overflow: hidden; }
  body { background: var(--stage); position: relative; font-family: "Roboto", sans-serif; }

  .card {
    position: absolute;
    border-radius: 6px;
    overflow: hidden;
  }

  /* Back side */
  .card--back {
    left: 82px; top: 139px; width: 484px; height: 293px;
    background: linear-gradient(180deg, var(--brand-blue) 0%, var(--brand-blue-dark) 100%);
    color: var(--on-blue);
    text-align: center;
  }
  .back__principles {
    position: absolute; left: 0; right: 0; top: 124px;
    font-family: "Roboto Condensed", sans-serif;
    font-size: 13.5px; letter-spacing: 0.1px;
  }
  .back__principles .sep { margin: 0 5px; }
  .back__promise {
    position: absolute; left: 0; right: 0; top: 147px;
    font-size: 15px;
  }

  /* Front side */
  .card--front {
    left: 602px; top: 138px; width: 481px; height: 291px;
    background: var(--card-white);
  }
  .front__brand {
    position: absolute; left: 10px; top: 130px; width: 205px;
    text-align: center;
    font-family: "Roboto", sans-serif;
    font-size: 23px; line-height: 1.1;
    color: var(--brand-blue-text);
  }
  .front__divider {
    position: absolute; left: 215px; top: 54px; width: 1px; height: 148px;
    background: var(--divider);
  }
  .front__name {
    position: absolute; left: 248px; top: 66px;
    font-family: "Exo 2", sans-serif; font-weight: 700;
    font-size: 21px; color: var(--brand-blue-text);
  }
  .front__title {
    position: absolute; left: 249px; top: 94px;
    font-size: 12.5px; color: var(--text-grey);
  }
  .contact-list {
    position: absolute; left: 250px; top: 122px;
    list-style: none;
    font-family: "Roboto Condensed", sans-serif;
    font-size: 12.5px; color: var(--text-grey);
  }
  .contact-list li { display: flex; align-items: center; height: 17px; }
  .contact-list svg { width: 11px; height: 11px; margin-right: 12px; fill: var(--brand-blue-text); }

  .front__base { position: absolute; left: 0; bottom: 0; width: 481px; height: 38px; }
  .front__tagline {
    position: absolute; right: 30px; bottom: 9px;
    font-size: 13.5px; color: var(--on-blue);
  }
</style>
</head>
<body>

  <section class="card card--back" aria-label="Card back">
    <p class="back__principles">Growth is Imperative<span class="sep">|</span>Change is Constant<span class="sep">|</span>Talent Executes Strategy</p>
    <p class="back__promise">We help you excel at all three.</p>
  </section>

  <section class="card card--front" aria-label="Card front">
    <div class="front__brand">Hollowmere<br>Advisory</div>
    <div class="front__divider"></div>
    <h1 class="front__name">Daniel Marsh</h1>
    <p class="front__title">Managing Director</p>
    <ul class="contact-list">
      <li><svg viewBox="0 0 12 12" aria-hidden="true"><path d="M3 0h6a1 1 0 0 1 1 1v10a1 1 0 0 1-1 1H3a1 1 0 0 1-1-1V1a1 1 0 0 1 1-1zm.5 1.5v8h5v-8zM6 10.2a.6.6 0 1 0 0 1.2.6.6 0 0 0 0-1.2z"/></svg>+1 415 208 3391</li>
      <li><svg viewBox="0 0 12 12" aria-hidden="true"><path d="M0 3.5C1.5 1.5 10.5 1.5 12 3.5v1.5H9V3.8C7.5 3.3 4.5 3.3 3 3.8V5H0zM3 6h6l2 5H1zm3 1.2a1.6 1.6 0 1 0 0 3.2 1.6 1.6 0 0 0 0-3.2z"/></svg>+1 415 208 3302</li>
      <li><svg viewBox="0 0 12 12" aria-hidden="true"><path d="M0 2h12v8H0zm1 1v.4l5 3.3 5-3.3V3zm0 1.6V9h10V4.6L6 7.9z"/></svg>person@HollowmereAdvisory.com</li>
      <li><svg viewBox="0 0 12 12" aria-hidden="true"><path d="M6 0a6 6 0 1 0 0 12A6 6 0 0 0 6 0zm-.6 1.1v2.3H3.7C4.1 2.1 4.7 1.3 5.4 1.1zm1.2 0c.7.2 1.3 1 1.7 2.3H6.6zM3.4 4.6h2v2.2H3.3zm3.2 0h2l.1 2.2H6.6zM1.2 4.6h1c0 .7 0 1.5.1 2.2h-1.1zm8.6 0h1a5 5 0 0 1 0 2.2H9.8zM3.6 8h1.8v2.9C4.6 10.7 4 9.6 3.6 8zm3 0h1.8c-.4 1.6-1 2.7-1.8 2.9z"/></svg>www.HollowmereAdvisory.com</li>
    </ul>
    <svg class="front__base" viewBox="0 0 481 38" aria-hidden="true">
      <rect x="0" y="19" width="200" height="19" fill="var(--slate)"/>
      <polygon points="214,0 481,0 481,38 188,38" fill="var(--brand-blue)"/>
    </svg>
    <p class="front__tagline">Optimize Your Investment in Talent</p>
  </section>

</body>
</html>
```